Wedding Invitation for a wedding at home - personal, romantic event

Want a wedding invitation that is to be printed onto card.
Size to be 148mm x 210mm
For it to open like a book not tent card
Have a picture of a house that I want to be the front cover.
I've attached 2 pictures. I like the picture without the man but with the grass
For the photo to become a drawing and the colours to be brighter.
If you could use the picture of us and get us in one of the windows.
If you could put the picture of the dog maybe somewhere on the grass.
Love the colour of the sky in the picture of the beach

Words to be on the inside of the card:
Together with our families
You are invited to the Wedding Reception of Tessa Wynford and Owen Pashley
On Saturday 9th of September 2017 at 6pm
At Pashley's Keep, 41b, Morrow Crescent, Camberley, Surrey, GU19 6QT
Carriages at 1am
RSVP by Friday 27th of July to 07700 915 268

Words on the Back page:
With all that we have, we've been truly blessed.
Your presence and prayers are all that we request.
But if you desire to give nonetheless,
Monetary gift is one we suggest.

If the pages can be white.
Writing in gold
gold border on all pages

Target Market(s)

Wedding guests

Industry/Entity Type

Wedding

Font styles to use
Script

Requirements
Must have
• Romantic feel. Our wedding colours are white, gold and rose gold.
• Designer to be creative and I do not have much inspiration.
Nice to have
• metallic colours
• Maybe have MR & MRS in gold metallic on the front page

```html
<!DOCTYPE html>
<html lang="en">
<head>
<meta charset="utf-8">
<title>Tessa &amp; Owen – Wedding Reception Invitation</title>
<link rel="stylesheet" href="https://fonts.googleapis.com/css2?family=Parisienne&display=swap">
<style>
  :root {
    --backdrop: #efe9e4;
    --page-white: #ffffff;
    --blush: #f4dde0;
    --blush-soft: #f9ecee;
    --ink-bronze: #8b5a2b;
    --name-bronze: #9a6a3c;
    --gold: #d9a93c;
    --frame-line: #e6d4d6;
    --house-warm: #d8b9a5;
    --house-light: #f3ebe6;
    --photo-skin: #d9b4a2;
    --photo-dark: #6e5a52;
  }
  * { margin: 0; padding: 0; box-sizing: border-box; }
  html, body { width: 1200px; height: 1000px; overflow: hidden; }
  body {
    background: var(--backdrop);
    font-family: "Parisienne", cursive;
    color: var(--ink-bronze);
    position: relative;
  }
  .spread {
    position: absolute;
    left: 20px;
    width: 1155px;
    height: 406px;
    background: var(--page-white);
    box-shadow: 0 2px 6px rgba(0,0,0,0.12);
    overflow: hidden;
  }
  .spread--outer { top: 107px; }
  .spread--inner { top: 547px; width: 1153px; }

  /* Outer spread: back page */
  .back-page {
    position: absolute; left: 0; top: 0; width: 578px; height: 100%;
  }
  .house-illustration {
    position: absolute; left: 135px; top: 18px; width: 340px; height: 345px;
    border-radius: 50%;
    background: radial-gradient(ellipse at 50% 45%, var(--house-warm) 0%, #e8d3c6 45%, var(--house-light) 70%, rgba(255,255,255,0) 100%);
    opacity: 0.85;
  }
  .blessing-verse {
    position: absolute; left: 0; top: 215px; width: 578px;
    text-align: center; font-size: 24px; line-height: 37px;
  }

  /* Outer spread: front cover */
  .front-cover {
    position: absolute; left: 578px; top: 0; width: 577px; height: 100%;
    background: var(--blush);
  }
  .cover-pattern {
    position: absolute; inset: 0;
    background: var(--blush);
  }
  .cover-nameplate {
    position: absolute; left: 88px; top: 86px; width: 400px; height: 233px;
    background: var(--page-white);
    border: 2px solid var(--frame-line);
  }
  .cover-names {
    position: absolute; color: var(--name-bronze); font-size: 50px; line-height: 1;
  }
  .cover-names--first { left: 68px; top: 56px; }
  .cover-names--amp   { left: 150px; top: 112px; }
  .cover-names--second{ left: 215px; top: 136px; }

  /* Inner spread */
  .inner-fade {
    position: absolute; left: 540px; top: 0; width: 300px; height: 100%;
    background: linear-gradient(to right, rgba(255,255,255,1) 0%, var(--blush-soft) 45%, var(--blush) 100%);
  }
  .couple-photo {
    position: absolute; left: 777px; top: 0; width: 376px; height: 100%;
    background: linear-gradient(110deg, var(--blush) 0%, var(--photo-skin) 35%, #c89a86 60%, var(--photo-dark) 100%);
  }
  .invitation-text {
    position: absolute; left: 0; top: 0; width: 580px; text-align: center;
  }
  .invitation-text .line { position: absolute; left: 0; width: 580px; white-space: nowrap; }
  .intro { font-size: 20px; }
  .couple-names { font-size: 40px; color: var(--name-bronze); }
  .event-date { font-size: 24px; }
  .venue { font-size: 22px; }
  .divider-dots {
    position: absolute; left: 188px; top: 236px;
  }
</style>
</head>
<body>

<section class="spread spread--outer">
  <div class="back-page">
    <div class="house-illustration" role="img" aria-label="Soft-faded illustration of the couple's red-brick family house"></div>
    <p class="blessing-verse">
      With all that we have, we've been truly blessed.<br>
      Your presence and prayers are all that we request.<br>
      But if you desire to give nonetheless,<br>
      Monetary gift is one we suggest.
    </p>
  </div>
  <div class="front-cover">
    <div class="cover-pattern" role="img" aria-label="Scattered gold heart-shaped petals on a blush background"></div>
    <div class="cover-nameplate">
      <span class="cover-names cover-names--first">Tessa</span>
      <span class="cover-names cover-names--amp">&amp;</span>
      <span class="cover-names cover-names--second">Owen</span>
    </div>
  </div>
</section>

<section class="spread spread--inner">
  <div class="inner-fade"></div>
  <div class="couple-photo" role="img" aria-label="Photograph of the couple together"></div>
  <div class="invitation-text">
    <p class="line intro" style="top:14px;">Together with our families</p>
    <p class="line intro" style="top:46px;">You are invited to the Wedding Reception of</p>
    <p class="line couple-names" style="top:104px;">Tessa Wynford and Owen Pashley</p>
    <p class="line event-date" style="top:180px;">On Saturday 9th of September 2017 at 6pm</p>
    <svg class="divider-dots" width="240" height="8" viewBox="0 0 240 8" aria-hidden="true">
      <g fill="var(--ink-bronze)">
        <circle cx="4" cy="4" r="2"/><circle cx="62" cy="4" r="2"/><circle cx="120" cy="4" r="2"/>
        <circle cx="178" cy="4" r="2"/><circle cx="236" cy="4" r="2"/>
      </g>
    </svg>
    <p class="line venue" style="top:264px;">At Pashley's Keep,</p>
    <p class="line venue" style="top:291px;">41b, Morrow Crescent, Camberley, Surrey, GU19 6QT</p>
    <p class="line venue" style="top:330px;">Carriages at 1am</p>
    <p class="line venue" style="top:359px;">RSVP by Friday 27th of July to 07700 915 268</p>
  </div>
</section>

</body>
</html>
```